Remo K Art Studio Business Card Layout

Hi, I have a logo but I need help laying it out on a business card. I would like to include the following:
The Logo (see attached)
remokartstudio.com
remo@remokartstudio.com

Industry/Entity Type

Business

```html
<!DOCTYPE html>
<html lang="en">
<head>
<meta charset="utf-8">
<title>Remo K Art Studio – Business Card</title>
<link rel="stylesheet" href="https://fonts.googleapis.com/css2?family=Open+Sans:wght@400;700&display=swap">
<style>
  :root {
    --backdrop: #2b2c2e;
    --card-paper: #fbfbf9;
    --gold: #b59c4c;
    --ink-olive: #8c7d42;
  }
  html, body {
    margin: 0;
    padding: 0;
    overflow: hidden;
  }
  body {
    width: 1200px;
    height: 800px;
    background: var(--backdrop);
    font-family: "Open Sans", Arial, sans-serif;
  }
  .business-card {
    position: absolute;
    left: 75px;
    top: 100px;
    width: 1050px;
    height: 600px;
    background: var(--card-paper);
    border-radius: 4px;
    overflow: hidden;
  }
  .brand-mark {
    position: absolute;
    left: 40px;
    top: 278px;
    width: 400px;
    display: flex;
    align-items: center;
    justify-content: center;
    gap: 12px;
  }
  .brand-mark__dot {
    width: 16px;
    height: 16px;
    border-radius: 50%;
    background: var(--gold);
    flex: none;
  }
  .brand-mark__name {
    font-weight: 400;
    font-size: 34px;
    color: var(--gold);
    white-space: nowrap;
  }
  .card-divider {
    position: absolute;
    left: 470px;
    top: 140px;
    width: 20px;
    height: 320px;
  }
  .contact-block {
    position: absolute;
    left: 530px;
    top: 180px;
    width: 480px;
    color: var(--ink-olive);
  }
  .contact-block__name {
    margin: 0;
    font-weight: 700;
    font-size: 46px;
    line-height: 1;
  }
  .contact-block__role {
    margin: 2px 0 16px;
    font-weight: 400;
    font-size: 28px;
    line-height: 1.1;
  }
  .contact-list {
    list-style: none;
    margin: 0;
    padding: 0;
  }
  .contact-list__item {
    display: flex;
    align-items: center;
    gap: 18px;
    font-size: 26px;
    line-height: 1;
    margin-bottom: 16px;
    white-space: nowrap;
  }
  .contact-list__icon {
    width: 26px;
    height: 26px;
    flex: none;
    display: flex;
    align-items: center;
    justify-content: center;
    font-weight: 700;
    font-size: 24px;
  }
</style>
</head>
<body>
  <article class="business-card">
    <div class="brand-mark">
      <span class="brand-mark__dot"></span>
      <span class="brand-mark__name">Remo K Art Studio</span>
    </div>

    <svg class="card-divider" viewBox="0 0 20 320" aria-hidden="true">
      <polygon points="3,0 6,0 18,320 15,320" fill="var(--gold)"/>
    </svg>

    <section class="contact-block">
      <h1 class="contact-block__name">John Doe</h1>
      <p class="contact-block__role">Director</p>
      <ul class="contact-list">
        <li class="contact-list__item">
          <span class="contact-list__icon">
            <svg viewBox="0 0 24 24" width="24" height="24" aria-hidden="true">
              <rect x="6" y="2" width="12" height="20" rx="2" fill="var(--ink-olive)"/>
              <rect x="8" y="5" width="8" height="12" fill="var(--card-paper)"/>
              <circle cx="12" cy="19.5" r="1.1" fill="var(--card-paper)"/>
            </svg>
          </span>
          <span>61400123987</span>
        </li>
        <li class="contact-list__item">
          <span class="contact-list__icon">
            <svg viewBox="0 0 24 24" width="22" height="22" aria-hidden="true">
              <circle cx="12" cy="12" r="10" fill="none" stroke="var(--ink-olive)" stroke-width="2"/>
              <ellipse cx="12" cy="12" rx="4.5" ry="10" fill="none" stroke="var(--ink-olive)" stroke-width="1.6"/>
              <line x1="2" y1="12" x2="22" y2="12" stroke="var(--ink-olive)" stroke-width="1.6"/>
            </svg>
          </span>
          <span>remokartstudio.com</span>
        </li>
        <li class="contact-list__item">
          <span class="contact-list__icon">@</span>
          <span>remo@remokartstudio.com</span>
        </li>
      </ul>
    </section>
  </article>
</body>
</html>
```